Corporate Web Redesign Project - coded

We would like redesign/refresh of our current site that would allow us to increase the depth of content and create a high quality impression for visitors.

Current site - http://corvanisystems.com/

A previous web redesign project has improved our site but it has not really reached the level we require.

Our customers are global, blue chip, organisations and a professional, corporate style of site is required.

Please note we would prefer a coded website to a just a design. We are happy to provide a zip of our current site if required.
Updates

                                   

Target Market(s)

Global oil and gas producers, KR, Tamberline, Orvadex etc.

Industry/Entity Type

It Professional

Requirements
Must have
• Design should support the level of content we currently have in the existing sitemap - although it should be expandable a site design for a large / complex site would not be appropriate

All current content / pages to be reflected in design

Must be visually appealing

Intuitive and clear navigation that is expandable

Display a high level of professionalism

Use a consistent palette of colours that complements our logo

Clean and organized layout

A way to capture visitor’s information or Call to action (i.e. contact link or form) on every page

Prominent Contact Information
Should not have
• Flash

```html
<!DOCTYPE html>
<html lang="en">
<head>
<meta charset="utf-8">
<title>Corvani Systems — The Business of Drilling Wells</title>
<link rel="stylesheet" href="https://fonts.googleapis.com/css2?family=Open+Sans:wght@300;400;600&family=Source+Sans+3:wght@400;600;700&display=swap">
<style>
  :root {
    --ink: #1d1d1d;
    --teal-dark: #1f5363;
    --teal-band: #215465;
    --teal-logo: #2a6f7c;
    --accent: #f5b21b;
    --accent-text: #f2b531;
    --sky: #7fd0ee;
    --panel: rgba(8, 10, 14, 0.86);
    --sky-top: #a9bfd8;
    --sky-low: #c9d6e4;
    --sea-top: #4f74a0;
    --sea-deep: #2e5585;
    --white: #ffffff;
  }
  * { box-sizing: border-box; margin: 0; padding: 0; }
  html, body { width: 1200px; height: 900px; overflow: hidden; background: var(--white); }
  body { font-family: "Open Sans", Arial, sans-serif; color: var(--ink); position: relative; }

  .site-header {
    position: absolute; left: 0; top: 0; width: 1200px; height: 100px;
    border-top: 4px solid var(--teal-dark);
    background: var(--white);
    box-shadow: 0 1px 3px rgba(0,0,0,0.15);
    z-index: 2;
  }
  .brand {
    position: absolute; left: 100px; top: 34px;
    display: flex; align-items: center; gap: 12px;
    font-family: "Source Sans 3", Arial, sans-serif;
    font-weight: 700; font-size: 24px; letter-spacing: 1px;
    color: var(--teal-logo);
  }
  .brand-mark { width: 30px; height: 30px; border-radius: 50%; background: var(--teal-logo); }
  .main-nav { position: absolute; top: 42px; left: 0; width: 1200px; }
  .main-nav a {
    position: absolute; font-size: 14px; color: var(--ink); text-decoration: none;
  }

  .hero-photo {
    position: absolute; left: 0; top: 100px; width: 1200px; height: 586px;
    background: linear-gradient(180deg, var(--sky-top) 0%, var(--sky-low) 26%, var(--sea-top) 29%, var(--sea-deep) 100%);
  }

  .solutions {
    position: absolute; left: 77px; top: 428px; width: 1047px; height: 258px;
    background: var(--panel);
  }
  .solution { position: absolute; top: 0; width: 250px; height: 258px; }
  .solution-icon {
    position: absolute; top: 22px; width: 60px; height: 60px;
    border: 2px solid var(--white); border-radius: 50%;
    display: flex; align-items: center; justify-content: center;
  }
  .solution-title {
    position: absolute; top: 105px; left: 0; width: 100%; text-align: center;
    font-family: "Source Sans 3", Arial, sans-serif; font-weight: 600;
    font-size: 19px; color: var(--accent-text);
  }
  .solution-text {
    position: absolute; top: 141px; font-size: 13px; line-height: 18px; color: var(--white);
  }
  .readmore-btn {
    position: absolute; top: 221px; height: 24px; padding: 0 5px;
    background: var(--accent); color: #111; font-size: 13px; line-height: 24px;
    text-decoration: none;
  }

  .intro-band {
    position: absolute; left: 0; top: 686px; width: 1200px; height: 169px;
    background: var(--teal-band); text-align: center;
    border-bottom: 4px solid #1a4552;
  }
  .intro-title { padding-top: 22px; font-weight: 300; font-size: 29px; line-height: 40px; color: var(--white); }
  .intro-text { margin-top: 2px; font-weight: 300; font-size: 20px; line-height: 24px; color: var(--sky); }
  .intro-link {
    display: inline-block; margin-top: 14px; font-size: 13px;
    color: var(--accent-text); text-decoration: underline;
  }

  .section-heading {
    position: absolute; top: 872px; font-size: 19px; color: #333; font-weight: 400;
  }
</style>
</head>
<body>
  <header class="site-header">
    <div class="brand"><span class="brand-mark"></span>CORVANI SYSTEMS</div>
    <nav class="main-nav">
      <a href="#" style="left:558px">HOME</a>
      <a href="#" style="left:666px">NEWS</a>
      <a href="#" style="left:750px">ABOUT US</a>
      <a href="#" style="left:869px">SOLUTIONS</a>
      <a href="#" style="left:990px">CONTACT US</a>
    </nav>
  </header>

  <div class="hero-photo" role="img" aria-label="Photograph of an offshore oil platform with cranes at sea under a cloudy sky"></div>

  <section class="solutions">
    <article class="solution" style="left:20px">
      <div class="solution-icon" style="left:94px">
        <svg width="24" height="24" viewBox="0 0 24 24" fill="#fff"><rect x="3" y="17" width="3" height="5"/><rect x="8" y="13" width="3" height="9"/><rect x="13" y="8" width="3" height="14"/><rect x="18" y="3" width="3" height="19"/></svg>
      </div>
      <h3 class="solution-title">Time &amp; Cost Estimation</h3>
      <p class="solution-text" style="left:24px;width:222px">TRV delivers a standardized, sys­tematic approach to understanding project risk.</p>
      <a class="readmore-btn" href="#" style="left:90px">readmore</a>
    </article>
    <article class="solution" style="left:273px">
      <div class="solution-icon" style="left:82px">
        <svg width="24" height="30" viewBox="0 0 20 26" fill="#fff"><rect x="1" y="1" width="18" height="24" rx="2"/><rect x="4" y="4" width="12" height="5" fill="#111"/><g fill="#111"><rect x="4" y="11" width="3" height="3"/><rect x="8.5" y="11" width="3" height="3"/><rect x="13" y="11" width="3" height="3"/><rect x="4" y="15.5" width="3" height="3"/><rect x="8.5" y="15.5" width="3" height="3"/><rect x="13" y="15.5" width="3" height="3"/><rect x="4" y="20" width="3" height="3"/><rect x="8.5" y="20" width="3" height="3"/><rect x="13" y="20" width="3" height="3"/></g></svg>
      </div>
      <h3 class="solution-title">Materials &amp; Cost Control</h3>
      <p class="solution-text" style="left:19px;width:212px">MVX has been helping companies optimize materials and cost track­ing processes since 1992.</p>
      <a class="readmore-btn" href="#" style="left:91px">readmore</a>
    </article>
    <article class="solution" style="left:520px">
      <div class="solution-icon" style="left:87px">
        <svg width="30" height="28" viewBox="0 0 30 28" fill="#fff"><path d="M3 8 L17 3 L27 8 L13 13 Z"/><path d="M3 12 L13 17 L27 12 L27 15 L13 20 L3 15 Z"/><path d="M3 19 L13 24 L27 19 L27 22 L13 27 L3 22 Z"/></svg>
      </div>
      <h3 class="solution-title">Lessons Learned</h3>
      <p class="solution-text" style="left:20px;width:226px;top:146px">LNX is an advanced lessons learned &amp; knowledge system for use in the energy industry.</p>
      <a class="readmore-btn" href="#" style="left:83px">readmore</a>
    </article>
    <article class="solution" style="left:770px">
      <div class="solution-icon" style="left:82px">
        <svg width="32" height="30" viewBox="0 0 32 30" fill="none" stroke="#fff"><circle cx="11" cy="19" r="6" stroke-width="5" stroke-dasharray="3 2.3"/><circle cx="11" cy="19" r="3" fill="#fff"/><circle cx="23" cy="9" r="4" stroke-width="4" stroke-dasharray="2.4 1.8"/><circle cx="23" cy="9" r="2" fill="#fff"/></svg>
      </div>
      <h3 class="solution-title">Services &amp; Consulting</h3>
      <p class="solution-text" style="left:27px;width:206px">Successful software implementa­tions rely on people and pro­cesses to deliver results.</p>
      <a class="readmore-btn" href="#" style="left:108px">readmore</a>
    </article>
  </section>

  <section class="intro-band">
    <h1 class="intro-title">The Business of Drilling Wells</h1>
    <p class="intro-text">For more than a decade Corvani Systems has been helping companies better<br>manage the Business of Drilling Wells.</p>
    <a class="intro-link" href="#">Readmore</a>
  </section>

  <h2 class="section-heading" style="left:101px">WHO WE ARE</h2>
  <h2 class="section-heading" style="left:736px">LATEST NEWS</h2>
</body>
</html>
```